Business Card design for new private practice opening

I need a business card design for my new private practice with my new logo uploaded as a file
On the front the logo
On the back: maybe a small logo somewhere?
Priv. Doz. DDr. Corinna Vestaluk
Fachärztin für Allgemein- & Viszeralchirurgie
Address: xxx
Tel: xxx
Mobil:xxx
Webseite:xxx
Email:xxx

Contact Information for Business Card

See project description above for details

Requirements
Nice to have
• I would like the colors of the logo incorporated into the business card

```html
<!DOCTYPE html>
<html lang="de">
<head>
<meta charset="utf-8">
<title>Vestaluk Chirurgie – Visitenkarte</title>
<link rel="stylesheet" href="https://fonts.googleapis.com/css2?family=Montserrat:wght@300;400;600;700&display=swap">
<style>
  :root {
    --teal: #45b8b5;
    --grey: #8a8a8a;
    --grey-dark: #7a7a7a;
    --paper: #ffffff;
    --backdrop: #dcdcdc;
  }
  * { margin: 0; padding: 0; box-sizing: border-box; }
  html, body { width: 1200px; height: 1200px; overflow: hidden; }
  body {
    background: var(--backdrop);
    font-family: "Montserrat", sans-serif;
    position: relative;
  }
  .card {
    position: absolute;
    left: 160px;
    width: 880px;
    height: 500px;
    background: var(--paper);
    border-radius: 44px;
    overflow: hidden;
  }
  .card--front { top: 70px; }
  .card--back { top: 630px; }

  /* Front */
  .front-mark {
    position: absolute;
    left: 50%; top: 50%;
    width: 190px; height: 190px;
    margin: -95px 0 0 -95px;
    border-radius: 50%;
    background: var(--teal);
  }

  /* Back */
  .brand {
    position: absolute;
    left: 50px; top: 54px;
    display: flex;
    align-items: center;
    gap: 20px;
  }
  .brand .dot {
    width: 90px; height: 90px;
    border-radius: 50%;
    background: var(--teal);
  }
  .brand .brand-name {
    color: var(--grey);
    font-weight: 600;
    font-size: 37px;
    line-height: 1.05;
    letter-spacing: 1px;
  }
  .divider {
    position: absolute;
    left: 445px; top: 120px;
    width: 2px; height: 280px;
    background: var(--teal);
  }
  .person {
    position: absolute;
    left: 96px; top: 232px;
  }
  .person .title { color: var(--grey); font-weight: 300; font-size: 22px; }
  .person .name { color: var(--grey-dark); font-weight: 600; font-size: 32px; line-height: 1.05; }
  .person .specialty { color: var(--teal); font-weight: 300; font-size: 19px; line-height: 1.15; margin-top: 6px; }

  .contact {
    position: absolute;
    left: 484px; top: 110px;
    list-style: none;
    color: var(--grey);
    font-weight: 300;
  }
  .contact .address { font-size: 19px; margin-left: 36px; margin-bottom: 6px; letter-spacing: 1px; }
  .contact li { display: flex; align-items: center; gap: 14px; height: 38px; font-size: 24px; letter-spacing: 1px; }
  .contact li.email { font-size: 21px; letter-spacing: 0; }
  .contact svg { width: 22px; height: 26px; flex: none; }

  .bands { position: absolute; left: 0; bottom: 0; width: 880px; height: 70px; }
  .web {
    position: absolute;
    left: 56px; bottom: 12px;
    color: var(--paper);
    font-weight: 600;
    font-size: 22px;
  }
</style>
</head>
<body>

<section class="card card--front" aria-label="Vorderseite">
  <span class="front-mark"></span>
</section>

<section class="card card--back" aria-label="Rückseite">
  <div class="brand">
    <span class="dot"></span>
    <span class="brand-name">VESTALUK<br>CHIRURGIE</span>
  </div>

  <div class="divider"></div>

  <div class="person">
    <p class="title">Priv. Doz. DDr.</p>
    <p class="name">Corinna Vestaluk</p>
    <p class="specialty">Fachärztin für Allgemein-<br>&amp; Viszeralchirurgie</p>
  </div>

  <ul class="contact">
    <p class="address">xxxx xxxx xx xxxxx xxxxxx</p>
    <li>
      <svg viewBox="0 0 22 26"><path d="M11 1C6 1 2 5 2 10c0 6 9 15 9 15s9-9 9-15c0-5-4-9-9-9z" fill="none" stroke="var(--teal)" stroke-width="3"/><circle cx="11" cy="10" r="3.2" fill="var(--teal)"/></svg>
      XXX XXX XXXX
    </li>
    <li>
      <svg viewBox="0 0 22 26"><path d="M4 6c1-2 3-2 4 0l2 3c0 2-2 2-2 3 1 3 3 5 5 6 1 0 1-2 3-2l3 2c2 1 1 3 0 4-3 3-9 0-13-5S1 9 4 6z" fill="var(--teal)"/></svg>
      XXX XXX XXXX
    </li>
    <li>
      <svg viewBox="0 0 22 26"><rect x="4" y="1" width="14" height="24" rx="2" fill="none" stroke="var(--teal)" stroke-width="2"/><circle cx="11" cy="21" r="1.4" fill="var(--teal)"/></svg>
      XXX XXX XXXX
    </li>
    <li class="email">
      <svg viewBox="0 0 22 26"><path d="M1 10h20v14H1z" fill="var(--teal)"/><path d="M1 10l10 8 10-8" fill="none" stroke="#fff" stroke-width="1.6"/><rect x="5" y="4" width="12" height="9" fill="#fff" stroke="var(--teal)" stroke-width="1.4"/></svg>
      cvestaluk@vestaluk-chirurgie.com
    </li>
  </ul>

  <svg class="bands" viewBox="0 0 880 70" aria-hidden="true">
    <polygon points="0,20 450,20 490,70 0,70" fill="var(--teal)"/>
    <rect x="490" y="22" width="390" height="16" fill="var(--grey)"/>
  </svg>
  <p class="web">www.vestaluk-chirurgie.com</p>
</section>

</body>
</html>
```